TRENDY & MODERN BUSINESS CARD DESIGN for Media Company *

I need a minimalistic - clean - modern and professional business card layout and design for MEDIA & PHOTOGRAPHY STUDIO.

We do NOT have a logo, and not really looking for one - but rather excellent typography and design. We would consider the 3 as a focal point.

We do personal and commercial photography.

Target Market(s)

Personal and commercial photography clientele

Contact Information for Business Card

ZUB size - from zub.com / size guidelines are enclosed in the brief

Font styles to use
Sans Serif

Colors
f78f20
eda3c7
cee9f5
0555a3
e667a6
fbf289

Requirements
Must have
• Clean lines - Modern layout
Nice to have
• All blue background as an option - use color palette in brief please.
Should not have
• Old fashion fonts and regular fonts.

```html
<!DOCTYPE html>
<html lang="en">
<head>
<meta charset="utf-8">
<title>Triad Lens Media – Business Card</title>
<link href="https://fonts.googleapis.com/css2?family=Fira+Sans+Extra+Condensed:wght@400;700&display=swap" rel="stylesheet">
<style>
  :root {
    --ice: #cee9f5;
    --royal: #0555a3;
    --blush: #eda3c7;
    --white: #ffffff;
  }
  html, body { margin: 0; padding: 0; overflow: hidden; }
  body {
    width: 1200px; height: 1200px;
    background: linear-gradient(90deg, #ffffff 0%, #9a9a9a 35%, #5a5a5a 65%, #000000 100%);
    position: relative;
    font-family: "Fira Sans Extra Condensed", "Arial Narrow", sans-serif;
  }
  .card { position: absolute; background: var(--ice); overflow: hidden; }
  .card p, .card h1 { margin: 0; line-height: 1; white-space: nowrap; position: absolute; }

  /* Front */
  .card-front { left: 200px; top: 68px; width: 800px; height: 456px; }
  .card-front .edge-top { position: absolute; left: 0; top: 0; width: 800px; height: 12px; background: var(--royal); }
  .card-front .edge-right { position: absolute; right: 0; top: 0; width: 16px; height: 456px; background: var(--royal); }
  .frame-lines { position: absolute; left: 0; top: 0; }
  .tagline { left: 54px; color: var(--royal); font-weight: 400; font-size: 110px; }
  .tagline-capturing { top: 38px; }
  .tagline-life { top: 208px; }
  .brand-name { color: var(--royal); font-weight: 700; text-transform: uppercase; letter-spacing: 1px; }
  .card-front .brand-name { left: 262px; top: 256px; font-size: 50px; }
  .holder-name { left: 42px; top: 346px; color: var(--royal); font-weight: 400; font-size: 62px; }

  /* Back */
  .card-back { left: 198px; top: 686px; width: 814px; height: 466px; }
  .blush-shape { position: absolute; left: -105px; top: -90px; width: 330px; height: 260px; border-radius: 50%; background: var(--blush); }
  .card-back .edge-top { position: absolute; left: 0; top: 0; width: 814px; height: 14px; background: var(--royal); }
  .card-back .edge-right { position: absolute; right: 0; top: 330px; width: 18px; height: 136px; background: var(--royal); }
  .contact-panel { position: absolute; left: 205px; top: 12px; width: 609px; height: 330px; background: var(--royal); border-bottom-left-radius: 150px; }
  .contact-line { color: var(--white); font-weight: 400; font-size: 30px; }
  .contact-icon { position: absolute; fill: var(--white); }
  .card-back .brand-name { left: 34px; top: 372px; font-size: 60px; }
</style>
</head>
<body>

<section class="card card-front" aria-label="Card front">
  <div class="edge-top"></div>
  <div class="edge-right"></div>
  <svg class="frame-lines" width="800" height="456" viewBox="0 0 800 456" fill="none" stroke="#0555a3" stroke-width="2">
    <polyline points="466,166 466,34 26,34 26,314 224,314 224,180"/>
    <rect x="222" y="180" width="428" height="146"/>
    <polyline points="650,326 26,326 26,428"/>
  </svg>
  <h1 class="tagline tagline-capturing">Capturing</h1>
  <p class="tagline tagline-life">Life</p>
  <p class="brand-name">Triad Lens Media</p>
  <p class="holder-name">Marisol Vega</p>
</section>

<section class="card card-back" aria-label="Card back">
  <div class="blush-shape"></div>
  <div class="edge-top"></div>
  <div class="edge-right"></div>
  <div class="contact-panel"></div>

  <svg class="contact-icon" style="left:337px;top:48px" width="36" height="66" viewBox="0 0 40 66">
    <path d="M20 0C9 0 0 9 0 20c0 12 20 46 20 46s20-34 20-46C40 9 31 0 20 0zm0 27a7 7 0 1 1 0-14 7 7 0 0 1 0 14z"/>
  </svg>
  <p class="contact-line" style="left:401px;top:19px">2450 Harbor Avenue</p>
  <p class="contact-line" style="left:401px;top:65px">9th Floor</p>
  <p class="contact-line" style="left:401px;top:111px">Coral Bay, FL 33100</p>

  <svg class="contact-icon" style="left:333px;top:152px" width="43" height="66" viewBox="0 0 44 66">
    <path d="M4 6c3-5 10-7 13-4l4 10c1 3-1 5-4 6-2 1-2 4-1 8 2 8 5 14 9 18 2 2 5 2 7 0 2-2 5-2 7 0l4 8c1 3-1 7-5 9-8 5-20 0-28-16C2 32 0 15 4 6z"/>
  </svg>
  <p class="contact-line" style="left:396px;top:178px">(305) 555-0148</p>

  <svg class="contact-icon" style="left:328px;top:258px" width="55" height="34" viewBox="0 0 56 34">
    <path d="M0 0h56L28 20z"/>
    <path d="M0 4v30h56V4L28 24z"/>
  </svg>
  <p class="contact-line" style="left:401px;top:261px">mv@triadlensmedia.com</p>

  <p class="brand-name">Triad Lens Media</p>
</section>

</body>
</html>
```